Updated Business Card for Optometry Practice

We're a growing optometry practice that is moving to a beautiful new office and we want to update our business card. We just updated our logo so the new card should reflect the new logo. Our practice continually invests in state of the art instruments to help us provide eye care that is thorough, comfortable, efficient and educational.

I've attached our current card and logo. You can reference this for the information I would like on the card. The tag line on the back is "We're changing the way you see."

Upon completion of this project we will need (amongst other formats) Photoshop files of the card so I can change employee names to print cards for each employee.

```html
<!DOCTYPE html>
<html lang="en">
<head>
<meta charset="utf-8">
<title>Brightwell Family Eyecare – Business Card</title>
<link rel="stylesheet" href="https://fonts.googleapis.com/css2?family=Inter:wght@400;500;600;700&display=swap">
<style>
  :root {
    --navy: #12284f;
    --navy-deep: #0f2346;
    --navy-light: #152e5a;
    --gold: #d4a72c;
    --gold-wash: rgba(232, 205, 140, 0.22);
    --gray-wash: rgba(200, 198, 212, 0.25);
    --white: #ffffff;
    --backdrop: #d3d4d6;
    --text-navy: #16244a;
  }
  * { box-sizing: border-box; margin: 0; padding: 0; }
  html, body {
    width: 900px; height: 1200px; overflow: hidden;
    background: var(--backdrop);
    font-family: "Inter", sans-serif;
  }
  .canvas { position: relative; width: 900px; height: 1200px; }

  .card { position: absolute; overflow: hidden; }

  /* Back side */
  .card-back {
    left: 135px; top: 213px; width: 629px; height: 359px;
    background: linear-gradient(135deg, var(--navy-deep), var(--navy-light));
  }
  .card-back .soft-glow {
    position: absolute; left: 120px; top: 30px; width: 400px; height: 260px;
    background: radial-gradient(ellipse at center, rgba(255,255,255,0.05), rgba(255,255,255,0) 70%);
  }
  .card-back .wordmark {
    position: absolute; left: 0; right: 0; top: 136px;
    display: flex; justify-content: center; align-items: center; gap: 14px;
  }
  .wordmark-dot {
    width: 26px; height: 26px; border-radius: 50%; background: var(--gold); flex: none;
  }
  .card-back .wordmark-name {
    color: var(--white); font-weight: 500; font-size: 36px; letter-spacing: 3px;
    text-transform: uppercase; line-height: 1.1;
  }
  .card-back .wordmark-name span { display: block; font-size: 20px; letter-spacing: 7.6px; }
  .tagline {
    position: absolute; left: 0; right: 0; top: 317px; text-align: center;
    color: var(--white); font-size: 14.5px; font-weight: 600; letter-spacing: 0.5px;
  }

  /* Front side */
  .card-front {
    left: 136px; top: 627px; width: 631px; height: 360px;
    background: var(--white);
  }
  .card-front .soft-glow {
    position: absolute; left: 360px; top: -20px; width: 300px; height: 260px;
    background:
      radial-gradient(circle at 62% 50%, var(--gray-wash), rgba(255,255,255,0) 45%),
      radial-gradient(ellipse at 55% 55%, var(--gold-wash), rgba(255,255,255,0) 70%);
  }
  .card-front .wordmark {
    position: absolute; left: 37px; top: 38px;
    display: flex; align-items: center; gap: 12px;
  }
  .card-front .wordmark-name {
    color: var(--navy); font-weight: 500; font-size: 29px; letter-spacing: 2px;
    text-transform: uppercase; line-height: 1.1;
  }
  .card-front .wordmark-name span { display: block; font-size: 16px; letter-spacing: 6.8px; }

  .person { position: absolute; left: 37px; top: 178px; }
  .person-name { color: var(--text-navy); font-size: 25px; font-weight: 700; }
  .person-title { color: var(--gold); font-size: 15px; font-weight: 600; margin-top: 4px; }

  .contact-list { position: absolute; left: 37px; top: 253px; list-style: none; }
  .contact-list li {
    display: flex; align-items: center; gap: 9px;
    color: var(--text-navy); font-size: 15px; height: 24.5px; letter-spacing: 0.6px;
  }
  .contact-list li.phone { letter-spacing: 2.6px; }
  .contact-list svg { width: 15px; height: 15px; fill: var(--gold); flex: none; }

  .address {
    position: absolute; right: 37px; top: 253px; text-align: right;
    color: var(--text-navy); font-size: 15px; line-height: 24.5px; font-style: normal;
  }
  .address .practice { color: var(--gold); font-weight: 500; }
</style>
</head>
<body>
<div class="canvas">

  <section class="card card-back" aria-label="Card back">
    <div class="soft-glow"></div>
    <div class="wordmark">
      <div class="wordmark-dot"></div>
      <div class="wordmark-name">Brightwell<span>Family Eyecare</span></div>
    </div>
    <p class="tagline">We're changing the way you see.</p>
  </section>

  <section class="card card-front" aria-label="Card front">
    <div class="soft-glow"></div>
    <div class="wordmark">
      <div class="wordmark-dot"></div>
      <div class="wordmark-name">Brightwell<span>Family Eyecare</span></div>
    </div>

    <div class="person">
      <h1 class="person-name">Daniel Marsh, OD</h1>
      <p class="person-title">Optometrist</p>
    </div>

    <ul class="contact-list">
      <li class="phone">
        <svg viewBox="0 0 24 24" aria-hidden="true"><path d="M6.6 10.8a15.1 15.1 0 0 0 6.6 6.6l2.2-2.2a1 1 0 0 1 1-.25 11.4 11.4 0 0 0 3.6.57 1 1 0 0 1 1 1V20a1 1 0 0 1-1 1A17 17 0 0 1 3 4a1 1 0 0 1 1-1h3.5a1 1 0 0 1 1 1c0 1.25.2 2.45.57 3.57a1 1 0 0 1-.25 1z"/></svg>
        (555) 014-2290
      </li>
      <li>
        <svg viewBox="0 0 24 24" aria-hidden="true"><path d="M2 5h20v14H2z M3.5 6.5 12 13l8.5-6.5" stroke="#fff" stroke-width="1.4"/></svg>
        dan@brightwelleyecare.com
      </li>
      <li>
        <svg viewBox="0 0 24 24" aria-hidden="true"><circle cx="12" cy="12" r="10"/><path d="M2 12h20M12 2c3 3 3 17 0 20M12 2c-3 3-3 17 0 20M4 7h16M4 17h16" stroke="#fff" stroke-width="1.2" fill="none"/></svg>
        www.brightwelleyecare.com
      </li>
    </ul>

    <address class="address">
      <div class="practice">Brightwell Family Eyecare</div>
      <div>2710 Linden Park Dr #204</div>
      <div>Maple Grove, MO 63999</div>
    </address>
  </section>

</div>
</body>
</html>
```